KALVERIA Consultancy Business Card

We need a business card design for a new Image & Etiquette Consultancy Company.

The design should reflect the corporate colour found in the logo attached.

Info to include:

Name: Melba Tran
Title: Image Consultant
Company: KAL VERIA CONSULTANCY
Address: 27 Kelso Street, #14-09 Harbourline Tower, Singapore 058217
Contact: 9317 6284
Email: melba@kalveria.com.sg
Website: www.kalveria.com.sg

```html
<!DOCTYPE html>
<html lang="en">
<head>
<meta charset="utf-8">
<title>KALVERIA Consultancy Business Card</title>
<link rel="stylesheet" href="https://fonts.googleapis.com/css2?family=Open+Sans:wght@400;600;700&display=swap">
<style>
  :root {
    --plum: #2c1446;
    --gold: #c9a23a;
    --ink: #1c1c1c;
    --card: #ffffff;
    --backdrop: #e7e3de;
  }
  * { margin: 0; padding: 0; box-sizing: border-box; }
  html, body {
    width: 1200px;
    height: 874px;
    overflow: hidden;
    background: var(--backdrop);
    font-family: "Open Sans", Arial, sans-serif;
    color: var(--ink);
  }
  .stage { position: relative; width: 1200px; height: 874px; }
  .card {
    position: absolute;
    width: 677px;
    height: 386px;
    background: var(--card);
  }
  .card--front { left: 66px; top: 32px; }
  .card--back { left: 472px; top: 450px; }

  .wordmark {
    position: absolute;
    left: 0; right: 0;
    text-align: center;
    font-weight: 400;
    color: var(--plum);
    letter-spacing: 4px;
    line-height: 1;
  }
  .card--front .wordmark { top: 92px; font-size: 54px; }
  .card--back .wordmark { top: 145px; font-size: 46px; }

  .name-band {
    position: absolute;
    left: 0; right: 0;
    top: 215px;
    height: 42px;
    background: var(--plum);
    color: #fff;
    display: flex;
    align-items: center;
    justify-content: center;
    gap: 7px;
  }
  .name-band .person { font-weight: 600; font-size: 20px; }
  .name-band .role { font-size: 16px; }

  .contact-list {
    position: absolute;
    left: 30px;
    top: 287px;
    list-style: none;
    font-size: 16px;
    line-height: 24px;
  }
  .contact-list li { display: flex; align-items: center; gap: 8px; }
  .contact-list svg { width: 14px; height: 14px; flex: none; }

  .address {
    position: absolute;
    right: 23px;
    top: 287px;
    text-align: right;
    font-size: 16px;
    line-height: 24px;
    font-style: normal;
  }

  .back-url {
    position: absolute;
    left: 0; right: 0;
    top: 318px;
    text-align: center;
    font-size: 20px;
  }
</style>
</head>
<body>
<main class="stage">
  <section class="card card--front" aria-label="Business card front">
    <div class="wordmark">KALVERIA</div>
    <div class="name-band">
      <span class="person">Melba Tran</span>
      <span class="role">Image Consultant</span>
    </div>
    <ul class="contact-list">
      <li>
        <svg viewBox="0 0 14 14" aria-hidden="true"><circle cx="7" cy="7" r="6.5" fill="none" stroke="var(--gold)"/><path d="M4.5 3.5 L6 3.5 L6.5 5.5 L5.6 6.2 Q6.6 8 7.8 8.4 L8.5 7.5 L10.5 8 L10.5 9.5 Q6 10 4.5 3.5Z" fill="var(--gold)"/></svg>
        <span>9317 6284</span>
      </li>
      <li>
        <svg viewBox="0 0 14 14" aria-hidden="true"><circle cx="7" cy="7" r="6.5" fill="none" stroke="var(--gold)"/><rect x="3.5" y="4.5" width="7" height="5" fill="none" stroke="var(--gold)"/><path d="M3.5 4.5 L7 7.5 L10.5 4.5" fill="none" stroke="var(--gold)"/></svg>
        <span>melba@kalveria.com.sg</span>
      </li>
      <li>
        <svg viewBox="0 0 14 14" aria-hidden="true"><circle cx="7" cy="7" r="6.5" fill="none" stroke="var(--gold)"/><ellipse cx="7" cy="7" rx="2.6" ry="6.5" fill="none" stroke="var(--gold)"/><path d="M0.5 7 H13.5" stroke="var(--gold)"/></svg>
        <span>www.kalveria.com.sg</span>
      </li>
    </ul>
    <address class="address">
      27 Kelso Street, #14-09<br>
      Harbourline Tower, Singapore<br>
      058217
    </address>
  </section>

  <section class="card card--back" aria-label="Business card back">
    <div class="wordmark">KALVERIA</div>
    <div class="back-url">www.kalveria.com.sg</div>
  </section>
</main>
</body>
</html>
```